A Real Estate Company Needs a Business Card Design

We need a business card design for a new company based in Boston MA called "Brackenfield Real Estate LLC" we are a small company but we like a big corporate look, a simple, sleek, modern and progressive look. we would like the option of having a design that could include the real estate agents personal photo and also a design if the realtor decides not to have a photo. we do not have LOGO at this moment, please use any property look pic corporate with word" Brackenfield Real Estate LLC" please see attached file as an example.
Industry/Entity Type
Business

```html
<!DOCTYPE html>
<html lang="en">
<head>
<meta charset="utf-8">
<title>Brackenfield Real Estate LLC – Business Cards</title>
<link href="https://fonts.googleapis.com/css2?family=Archivo:wght@700&display=swap" rel="stylesheet">
<style>
  :root {
    --taupe: #a89886;
    --taupe-dark: #7f7266;
    --sand: #e6d3b9;
    --paper: #ffffff;
    --photo-tone: #d9cfc4;
  }
  html, body {
    margin: 0;
    padding: 0;
    width: 1200px;
    height: 1000px;
    overflow: hidden;
    background: var(--paper);
  }
  .sheet {
    display: block;
    width: 1200px;
    height: 1000px;
  }
  .sheet text {
    font-family: "Archivo", "Helvetica Neue", Arial, sans-serif;
    font-weight: 700;
    fill: var(--taupe-dark);
  }
  .band { fill: var(--taupe); }
  .hill { fill: var(--sand); }
  .card-back { fill: var(--paper); }
  .divider { stroke: var(--taupe); stroke-width: 4; }
  .brand-mark { fill: var(--taupe-dark); }
  .photo-frame { fill: var(--photo-tone); stroke: var(--taupe-dark); stroke-width: 5; }
</style>
</head>
<body>
<svg class="sheet" viewBox="0 0 1200 1000" xmlns="http://www.w3.org/2000/svg">

  <!-- Front of card -->
  <g class="card-front">
    <rect class="band" x="320" y="137" width="583" height="332"/>
    <path class="hill" d="M320 365 Q600 240 903 375 L903 469 L320 469 Z"/>
    <rect class="brand-mark" x="581" y="180" width="60" height="60"/>
    <text class="brand-name" x="611" y="390" font-size="48" text-anchor="middle" textLength="400" lengthAdjust="spacingAndGlyphs">BRACKENFIELD</text>
    <text class="brand-name" x="611" y="437" font-size="40" text-anchor="middle">Real Estate LLC</text>
  </g>

  <!-- Back of card, no photo -->
  <g class="card-back-plain">
    <rect class="card-back" x="9" y="515" width="584" height="333"/>
    <path class="band" d="M9 515 L120 515 Q230 680 110 848 L9 848 Z"/>
    <line class="divider" x1="166" y1="605" x2="593" y2="605"/>
    <rect class="brand-mark" x="200" y="545" width="36" height="36"/>
    <text class="brand-name" x="562" y="561" font-size="28" text-anchor="end" textLength="300" lengthAdjust="spacingAndGlyphs">BRACKENFIELD</text>
    <text class="brand-name" x="558" y="588" font-size="24" text-anchor="end">Real Estate LLC</text>
    <text class="agent-name" x="212" y="681" font-size="40">Your Name</text>
    <text class="agent-position" x="212" y="722" font-size="27">your position</text>
    <text class="contact" x="212" y="801" font-size="16.5">phone: 123 456 789</text>
    <text class="contact" x="212" y="824" font-size="16.5">email: yourname@domain.com</text>
  </g>

  <!-- Back of card, with agent photo -->
  <g class="card-back-photo">
    <rect class="card-back" x="608" y="515" width="584" height="333"/>
    <path class="band" d="M608 515 L718 515 Q830 680 690 848 L608 848 Z"/>
    <line class="divider" x1="765" y1="605" x2="1192" y2="605"/>
    <rect class="photo-frame" x="627.5" y="599.5" width="120" height="163" role="img" aria-label="Agent portrait photo"/>
    <rect class="brand-mark" x="799" y="545" width="36" height="36"/>
    <text class="brand-name" x="1160" y="561" font-size="28" text-anchor="end" textLength="300" lengthAdjust="spacingAndGlyphs">BRACKENFIELD</text>
    <text class="brand-name" x="1157" y="588" font-size="24" text-anchor="end">Real Estate LLC</text>
    <text class="agent-name" x="811" y="681" font-size="40">Your Name</text>
    <text class="agent-position" x="811" y="722" font-size="27">your position</text>
    <text class="contact" x="811" y="801" font-size="16.5">phone: 123 456 789</text>
    <text class="contact" x="811" y="824" font-size="16.5">email: yourname@domain.com</text>
  </g>

</svg>
</body>
</html>
```